Fahnendesign für Lenk & Stabe Elektrotechnik
Zielgruppe
Lenk & Stabe Elektrotechnik hat sich spezialisiert auf die Errichtung elektrischer Anlagen im Wohn-Neubau und bei Sanierungen von Wohnungen und Einfamilienhäusern. Unsere Zielgruppe sind Bauunternehmen und private Bauherren.
Aufgabenstellung
-Design nach Vorgaben Druckfalter ( Befestigung links )
Natürlich soll unser Logo gut zu sehen sein sowie unsere Internetseite : www.lenk-stabe.de
Firmenschriftart: Titel Fira Sans , Schrift : Montserrat
Vielleicht kann ein Bezug auf die Positionierung hergestellt werden , ist aber kein muss.
Alles andere kann kreativ entschieden werden. Schaut gerne auf unsere Social Media Kanäle:
https://www.instagram.example/lenk_stabe_elektrotechnik/?hl=de
https://www.facebook.example/lenkstabeelektrotechnik/

```html
<!DOCTYPE html>
<html lang="de">
<head>
<meta charset="utf-8">
<title>Lenk &amp; Stabe Elektrotechnik – Fahnendesigns</title>
<link rel="stylesheet" href="https://fonts.googleapis.com/css2?family=Fira+Sans:wght@600&family=Montserrat:wght@500;600&display=swap">
<style>
  :root {
    --brand-blue: #5593cf;
    --text-grey: #4a4a4a;
    --flag-white: #ffffff;
    --stage: #e8eaec;
    --dot-light: #f1f1f1;
    --dot-mid: #d6d6d6;
  }
  * { box-sizing: border-box; margin: 0; padding: 0; }
  html, body { width: 1200px; height: 800px; overflow: hidden; }
  body {
    background: var(--stage);
    font-family: "Montserrat", sans-serif;
    position: relative;
  }
  .flag {
    position: absolute;
    top: 80px;
    width: 240px;
    height: 640px;
    background: var(--flag-white);
    box-shadow: 0 2px 10px rgba(0,0,0,.12);
    overflow: hidden;
  }
  .flag--edge-repeat { left: 48px; }
  .flag--pattern { left: 336px; }
  .flag--vertical { left: 624px; }
  .flag--classic { left: 912px; }

  .mark-circle {
    display: block;
    border: 3px solid var(--brand-blue);
    border-radius: 50%;
    margin: 0 auto;
  }
  .wordmark {
    font-family: "Fira Sans", sans-serif;
    font-weight: 600;
    color: var(--brand-blue);
    text-align: center;
    line-height: 1.15;
    letter-spacing: .04em;
  }
  .wordmark span { display: block; }
  .url {
    font-weight: 500;
    color: var(--text-grey);
    text-align: center;
  }

  /* Flag 1: repeated name along the pole edge */
  .edge-strip {
    position: absolute;
    left: 0; top: 0;
    width: 26px; height: 100%;
    display: flex;
    flex-direction: column;
    justify-content: space-around;
    align-items: center;
  }
  .edge-strip .edge-name {
    writing-mode: vertical-rl;
    transform: rotate(180deg);
    font-family: "Fira Sans", sans-serif;
    font-weight: 600;
    font-size: 8px;
    letter-spacing: .05em;
    color: var(--brand-blue);
    white-space: nowrap;
  }
  .flag--edge-repeat .center-block {
    position: absolute;
    left: 26px; right: 0; top: 250px;
  }
  .flag--edge-repeat .mark-circle { width: 64px; height: 64px; border-width: 2px; }
  .flag--edge-repeat .wordmark { font-size: 14px; margin-top: 14px; }
  .flag--edge-repeat .wordmark .sub { font-size: 6px; letter-spacing: .2em; }
  .flag--edge-repeat .url { font-size: 7px; margin-top: 14px; }

  /* Flag 2: patterned background with web band */
  .pattern-fill {
    position: absolute; inset: 0;
    background: radial-gradient(circle at 50% 45%, var(--dot-light), var(--dot-mid));
  }
  .flag--pattern .center-block {
    position: absolute; left: 0; right: 0; top: 150px;
  }
  .flag--pattern .mark-circle {
    width: 130px; height: 130px;
    background: var(--flag-white);
  }
  .flag--pattern .wordmark {
    font-size: 20px; margin-top: 20px;
    background: var(--flag-white);
    padding: 6px 0;
  }
  .flag--pattern .wordmark .sub { font-size: 8px; letter-spacing: .25em; }
  .web-band {
    position: absolute; left: 0; right: 0; top: 570px;
    height: 32px;
    background: var(--brand-blue);
    color: var(--flag-white);
    font-weight: 600;
    font-size: 18px;
    line-height: 32px;
    text-align: center;
  }

  /* Flag 3: vertical name */
  .vertical-name {
    position: absolute;
    left: 50%; top: 30px;
    transform: translateX(-50%);
    display: flex;
    gap: 8px;
    height: 400px;
  }
  .vertical-name .line {
    writing-mode: vertical-rl;
    transform: rotate(180deg);
    font-family: "Fira Sans", sans-serif;
    font-weight: 600;
    color: var(--brand-blue);
    white-space: nowrap;
    text-align: center;
  }
  .vertical-name .main { font-size: 40px; letter-spacing: .04em; }
  .vertical-name .sub { font-size: 11px; letter-spacing: .3em; }
  .flag--vertical .foot {
    position: absolute; left: 0; right: 0; top: 500px;
  }
  .flag--vertical .mark-circle { width: 60px; height: 60px; }
  .flag--vertical .url { font-size: 8px; margin-top: 22px; }

  /* Flag 4: classic upright */
  .flag--classic .center-block {
    position: absolute; left: 0; right: 0; top: 100px;
  }
  .flag--classic .mark-circle { width: 180px; height: 180px; border-width: 4px; }
  .flag--classic .wordmark { font-size: 24px; margin-top: 34px; }
  .flag--classic .wordmark .sub { font-size: 10px; letter-spacing: .28em; margin-top: 4px; }
  .flag--classic .url {
    position: absolute; left: 0; right: 0; top: 580px;
    font-size: 15px;
  }
</style>
</head>
<body>

<section class="flag flag--edge-repeat" aria-label="Fahne mit Namensleiste">
  <div class="edge-strip">
    <span class="edge-name">LENK &amp; STABE · ELEKTROTECHNIK</span>
    <span class="edge-name">LENK &amp; STABE · ELEKTROTECHNIK</span>
    <span class="edge-name">LENK &amp; STABE · ELEKTROTECHNIK</span>
    <span class="edge-name">LENK &amp; STABE · ELEKTROTECHNIK</span>
  </div>
  <div class="center-block">
    <span class="mark-circle"></span>
    <p class="wordmark"><span>LENK &amp; STABE</span><span class="sub">ELEKTROTECHNIK</span></p>
    <p class="url">www.lenk-stabe.de</p>
  </div>
</section>

<section class="flag flag--pattern" aria-label="Fahne mit Punktmuster">
  <div class="pattern-fill" role="img" aria-label="Dekoratives graues Punktraster als Hintergrund"></div>
  <div class="center-block">
    <span class="mark-circle"></span>
    <p class="wordmark"><span>LENK &amp; STABE</span><span class="sub">ELEKTROTECHNIK</span></p>
  </div>
  <p class="web-band">www.lenk-stabe.de</p>
</section>

<section class="flag flag--vertical" aria-label="Fahne mit senkrechtem Namen">
  <div class="vertical-name">
    <span class="line main">LENK &amp; STABE</span>
    <span class="line sub">ELEKTROTECHNIK</span>
  </div>
  <div class="foot">
    <span class="mark-circle"></span>
    <p class="url">www.lenk-stabe.de</p>
  </div>
</section>

<section class="flag flag--classic" aria-label="Fahne klassisch">
  <div class="center-block">
    <span class="mark-circle"></span>
    <p class="wordmark"><span>LENK &amp; STABE</span><span class="sub">ELEKTROTECHNIK</span></p>
  </div>
  <p class="url">www.lenk-stabe.de</p>
</section>

</body>
</html>
```